Hi, everyone!

We're looking for a tenacious designer to help us create two (2) 33 x 86 single-sided retractable banners. The banners will be purchased through
Bannerloft (see: https://www.bannerloft-example.ca/signs-posters/retractable-banners?xnav=swsProductOnly_ResultTitle).

I have attached a wide variety of materials including the Plovrix - Creative Production logos (.psd files), previous attempts at making a banner including some handwritten notes and a table cloth that will be used in the same space as the banners and the back of our business card to give you an idea of our colours.

Note: We like the colours used on the other banner designs but do not like the layout or icons - they look cluttered and unprofessional. They are good as a guide but not what we want as a design. Similarly, avoid featuring close-ups of people from stock photos.

At least one of the banners must feature: (you can use icons instead of words if it means a better design)

www.plovrix-example.ca
Email: get@plovrix-example.ca
Phone: (555) 214-0873
Social Media Handle: plovrixstudio

There is also a word document on the bottom to guide some of the copywriting that may be used. If you're really ambitious, we're happy to consider different phrases and copy.

Finally, the fonts that we use are:
Plovrix Logo - Metropolis
Titles: Adelle Font Family
Body / Content: Avenir Font Family

As with everything, we welcome other suggestions or recommendations.

Target Market(s)

Government, Small Business, Non-Profits, Indigenous Canadian Communities

Font styles to use
Sans Serif

Colors

Designer to choose colors to be used in the design.

Requirements
Must have
• The deliverables for this project are:
• - Two (2) 33 x 86 Single-Sided Retractable Banners
• They will be purchased through Bannerloft Canada (see: https://www.bannerloft-example.ca/signs-posters/retractable-banners?xnav=swsProductOnly_ResultTitle). You may want to try loading your design there before submitting them to us.
Nice to have
• We like the colours of the initial designs but they are unprofessional, cluttered and from a template. Ideally, we would like a unique design that works with the colours in our logo (red, black, white and yellow).
• One banner may focus on Tourism Development and the other could feature Creative Strategy.
Should not have
• Please do not use stock photos that feature people - our target market is put off by such pictures. If you'd like an idea of our tourism focus, visit:
• - https://northwoodtravelcircle-example.ca/en/
• - https://lakeheadjourneys-example.ca/
• - https://www.qolfa-example.org/

```html
<!DOCTYPE html>
<html lang="en">
<head>
<meta charset="utf-8">
<title>Plovrix Creative Productions – Retractable Banners</title>
<link rel="stylesheet" href="https://fonts.googleapis.com/css2?family=Zilla+Slab:wght@600;700&family=Mulish:wght@400;500;700;800&display=swap">
<style>
  :root{
    --red:#a3222f;
    --yellow:#e8b316;
    --orange:#e89a2a;
    --ink:#1c1a1a;
    --grey-text:#4a4a4a;
    --panel-top:#ffffff;
    --panel-bottom:#dcdcdc;
    --page:#ffffff;
  }
  *{box-sizing:border-box;margin:0;padding:0}
  html,body{width:1200px;height:1200px;overflow:hidden;background:var(--page)}
  body{position:relative;font-family:"Mulish",sans-serif;color:var(--ink)}

  .banner{position:absolute;top:71px;width:394px;height:1027px;overflow:hidden;
    background:linear-gradient(180deg,var(--panel-top) 0%,var(--panel-top) 55%,var(--panel-bottom) 93%)}
  .banner--strategy{left:154px}
  .banner--approach{left:660px;background:linear-gradient(180deg,#e6e6e6 35%,#ffffff 60%,#ffffff 100%)}
  .banner-art{position:absolute;left:0;top:0;width:394px;height:620px}

  .brand{position:absolute;top:60px;right:18px;display:flex;align-items:center;gap:8px}
  .brand-dot{width:14px;height:14px;border-radius:50%;background:var(--red)}
  .brand-name{font-family:"Mulish",sans-serif;font-weight:800;font-size:30px;color:#fff;letter-spacing:.5px;line-height:1}

  .headline{position:absolute;left:20px;font-family:"Zilla Slab",serif;font-weight:700;color:var(--ink)}
  .banner--strategy .headline{top:504px;font-size:39px;line-height:36px}
  .banner--approach .headline{top:474px;font-size:31px;line-height:28.5px}
  .kicker{position:absolute;left:20px;font-family:"Zilla Slab",serif;font-weight:600;color:var(--red)}
  .banner--strategy .kicker{top:628px;font-size:20.5px;letter-spacing:.2px}
  .banner--approach .kicker{top:569px;font-size:17.5px}
  .intro{position:absolute;left:20px;right:20px;text-align:justify;font-weight:500}
  .banner--strategy .intro{top:657px;font-size:11.6px;line-height:12.6px}
  .banner--approach .intro{top:603px;font-size:9.6px;line-height:11px;right:32px}

  .help-rule{position:absolute;left:29px;right:29px;height:1px;background:var(--red)}
  .help-tab{position:absolute;left:96px;top:731px;width:203px;height:34px;background:var(--red);border-radius:6px 6px 0 0;
    color:#fff;font-weight:800;font-size:16px;display:flex;align-items:center;justify-content:center}
  .services{position:absolute;left:0;right:0;top:772px;list-style:none;text-align:center;font-size:15.3px;line-height:18.7px;font-weight:400}
  .home-note{position:absolute;left:18px;right:18px;top:895px;text-align:center;font-size:9.6px;line-height:12.3px;color:var(--grey-text)}

  .approach-tab{position:absolute;left:20px;top:665px;width:163px;height:28px;background:var(--orange);border-radius:5px 5px 0 5px;
    font-weight:800;font-size:17px;padding-left:21px;display:flex;align-items:center;color:var(--ink)}
  .approach-rule{position:absolute;left:183px;right:29px;top:677px;height:2px;background:var(--orange)}
  .step{position:absolute;left:0;right:0}
  .step-icon{position:absolute;left:37px;width:25px;height:25px}
  .step-label{position:absolute;left:20px;width:58px;text-align:center;font-weight:800;font-size:8.5px}
  .step-text{position:absolute;left:79px;right:32px;font-size:8.6px;line-height:9.2px;text-align:justify}
  .step-text p+p{margin-top:8px}

  .footer{position:absolute;left:0;right:0;top:955px;height:56px;background:var(--red);border-top:4px solid var(--orange)}
  .banner--strategy .footer::after{content:"";position:absolute;left:0;right:0;top:52px;height:20px;background:#dadada}
  .social{position:absolute;left:90px;top:8px;display:flex;gap:6px}
  .social span{width:15px;height:15px;border-radius:4px;background:var(--yellow)}
  .handle{position:absolute;left:124px;top:27px;font-weight:800;font-size:7.6px;color:var(--yellow)}
  .footer-divider{position:absolute;left:199px;top:5px;width:1px;height:36px;background:var(--yellow)}
  .contacts{position:absolute;left:208px;top:6px;list-style:none;font-weight:800;font-size:7.8px;line-height:10.4px;color:var(--yellow)}
  .contacts li{display:flex;align-items:center;gap:6px}
  .contacts li::before{content:"";width:7px;height:7px;border-radius:2px;background:var(--yellow)}
</style>
</head>
<body>

<section class="banner banner--strategy">
  <svg class="banner-art" viewBox="0 0 394 620" aria-hidden="false">
    <defs>
      <linearGradient id="dusk" x1="0" y1="0" x2="0" y2="1">
        <stop offset="0" stop-color="#2e2a28"/>
        <stop offset=".45" stop-color="#6c5a3e"/>
        <stop offset=".62" stop-color="#d96a2a"/>
        <stop offset=".75" stop-color="#2a2420"/>
        <stop offset="1" stop-color="#111"/>
      </linearGradient>
      <linearGradient id="gold-l" x1="0" y1="0" x2="1" y2="1">
        <stop offset="0" stop-color="#f0c419"/><stop offset="1" stop-color="#e09a26"/>
      </linearGradient>
      <linearGradient id="shade-l" x1="0" y1="0" x2="1" y2="1">
        <stop offset="0" stop-color="#fff"/><stop offset="1" stop-color="#333"/>
      </linearGradient>
    </defs>
    <path role="img" aria-label="Photograph of silhouetted spruce trees against an orange sunset over a lake"
      fill="url(#dusk)" d="M0 0H394V540C350 480 290 440 220 420C120 395 40 360 0 279Z"/>
    <path fill="#fff" d="M0 282C60 390 180 410 280 450C340 480 375 530 394 575V620H0Z"/>
    <path fill="url(#shade-l)" d="M6 300C40 410 150 480 262 505C160 470 70 420 6 300Z"/>
    <path fill="url(#gold-l)" d="M0 280C70 370 200 400 290 430C350 455 380 520 394 575C360 525 320 500 280 488C180 455 60 400 0 280Z"/>
    <path fill="var(--red)" d="M0 286C40 380 150 455 277 502C210 440 90 390 0 286Z"/>
  </svg>
  <div class="brand"><span class="brand-dot"></span><span class="brand-name">PLOVRIX</span></div>

  <h1 class="headline">Creative,<br>Culturally Inspired<br>Strategy</h1>
  <p class="kicker">WE START WITH YOUR STORY</p>
  <p class="intro">At Plovrix we start with your story. It enables us to create a deeper connection, unite people and drives meaningful growth. As your Indigenous marketing, communication and event partner, we use the power of story to learn, share, elevate and innovate.</p>

  <div class="help-rule" style="top:748px"></div>
  <h2 class="help-tab">How Can We Help?</h2>
  <ul class="services">
    <li>Destination and Product Development</li>
    <li>Media and Marketing</li>
    <li>Event Management and Planning</li>
    <li>Brand Development</li>
    <li>Graphic, Print and Web Design</li>
  </ul>
  <div class="help-rule" style="top:879px"></div>
  <p class="home-note">Based in Northwestern Ontario<br>at the foot of AnimkiiWajiw (“Thunder Mountain” or “Mount McKay”)<br>we're ready to tell your story through our globally informed skillset tailored<br>for meaningful and measurable local results.</p>

  <footer class="footer">
    <div class="social"><span></span><span></span><span></span><span></span><span></span></div>
    <span class="handle">@plovrixstudio</span>
    <div class="footer-divider"></div>
    <ul class="contacts">
      <li>plovrix-example.ca/tourism</li>
      <li>(555) 214-0873</li>
      <li>get@plovrix-example.ca</li>
    </ul>
  </footer>
</section>

<section class="banner banner--approach">
  <svg class="banner-art" viewBox="0 0 394 620">
    <defs>
      <linearGradient id="sky" x1="0" y1="0" x2="0" y2="1">
        <stop offset="0" stop-color="#3f5f8e"/>
        <stop offset=".35" stop-color="#9aa6b2"/>
        <stop offset=".55" stop-color="#e8a53a"/>
        <stop offset=".75" stop-color="#8a6a58"/>
        <stop offset="1" stop-color="#b7a89c"/>
      </linearGradient>
    </defs>
    <path fill="var(--red)" d="M0 292C60 420 200 485 394 498V385C250 420 100 400 0 292Z"/>
    <path fill="var(--orange)" d="M0 275C60 400 220 452 394 440V380C250 410 90 390 0 275Z"/>
    <path fill="var(--yellow)" d="M0 262C60 380 220 430 394 392V360C250 395 90 370 0 262Z"/>
    <path role="img" aria-label="Photograph of a stacked stone cairn on a mountain top at sunset under a blue sky"
      fill="url(#sky)" d="M0 0H394V361C300 398 220 406 150 388C80 365 20 315 0 255Z"/>
  </svg>
  <div class="brand"><span class="brand-dot"></span><span class="brand-name">PLOVRIX</span></div>

  <h1 class="headline">Creating<br>Meaningful Experiences<br>through Problem-Solving</h1>
  <p class="kicker">Redefining Engagement for Real Outcomes</p>
  <p class="intro">Our context informs our needs. Our experience and backgrounds in tourism and community development, outdoor recreation, marketing, film production, project management and design ensure those needs are met.</p>

  <h2 class="approach-tab">Our Approach</h2>
  <div class="approach-rule"></div>

  <div class="step">
    <svg class="step-icon" style="top:701px" viewBox="0 0 24 24"><circle cx="12" cy="12" r="12" fill="var(--red)"/><circle cx="13.5" cy="10.5" r="4" fill="none" stroke="var(--yellow)" stroke-width="1.6"/><path d="M10.6 13.4 7 17" stroke="var(--yellow)" stroke-width="1.8" stroke-linecap="round"/></svg>
    <span class="step-label" style="top:730px">DISCOVER</span>
    <div class="step-text" style="top:711px"><p>We're adventures at heart. Our inquisitive nature, cultural knowledge and perspective allows us to understand a challenge and find a suitable solution.</p></div>
  </div>
  <div class="step">
    <svg class="step-icon" style="top:748px" viewBox="0 0 24 24"><circle cx="12" cy="12" r="12" fill="var(--ink)"/><circle cx="12" cy="12" r="6.5" fill="none" stroke="var(--yellow)" stroke-width="1.3"/><circle cx="12" cy="12" r="3.5" fill="none" stroke="var(--yellow)" stroke-width="1.3"/><circle cx="12" cy="12" r="1" fill="var(--yellow)"/></svg>
    <span class="step-label" style="top:777px">DEFINE</span>
    <div class="step-text" style="top:758px">
      <p>Our company comes from a desire to create real outcomes. We work to understand the challenges and opportunities that real people encounter in their lives.</p>
      <p>We empower our clients through collective creativity. Our processes your first-hand experience and perspective are included throughout the problem-solving process.</p>
      <p>Your experience is at the core of our services. Shaped by our experience in the hospitality industry so all services made are accessible, and customer-focused.</p>
    </div>
  </div>
  <div class="step">
    <svg class="step-icon" style="top:858px" viewBox="0 0 24 24"><circle cx="12" cy="12" r="12" fill="var(--red)"/><circle cx="12" cy="10.5" r="4" fill="none" stroke="var(--yellow)" stroke-width="1.5"/><path d="M10 16h4M10.5 18h3" stroke="var(--yellow)" stroke-width="1.4" stroke-linecap="round"/></svg>
    <span class="step-label" style="top:888px">DESIGN</span>
    <div class="step-text" style="top:870px;left:80px"><p>Opportunities understanding of observed, human need. The services we provided are all focused on meaningful and useful experiences for people.</p></div>
  </div>
  <div class="step">
    <svg class="step-icon" style="top:910px" viewBox="0 0 24 24"><circle cx="12" cy="12" r="12" fill="var(--ink)"/><path d="M7 17 17 7M12 7h5v5" fill="none" stroke="var(--yellow)" stroke-width="1.8" stroke-linecap="round" stroke-linejoin="round"/></svg>
    <span class="step-label" style="top:940px">DELIVER</span>
    <div class="step-text" style="top:917px;left:80px"><p>We provide services across the entire customer journey. Our services all present an opportunity to learn more and build on.</p></div>
  </div>

  <footer class="footer">
    <div class="social"><span></span><span></span><span></span><span></span><span></span></div>
    <span class="handle">@plovrixstudio</span>
    <div class="footer-divider"></div>
    <ul class="contacts">
      <li>plovrix-example.ca/tourism</li>
      <li>(555) 214-0873</li>
      <li>get@plovrix-example.ca</li>
    </ul>
  </footer>
</section>

</body>
</html>
```